Business Card Design

Contact Information for Business Card

A vertical business card request- a medium & light gray with silverfern tree logo (logo is attached)

Please use Trebuchet font -- if possible- can we use two different color gray? (See pictures attached below)
Info on the front should be the Silverfern tree logo - on the top of the card, followed by the info ...
Card to read: " " indicated what should be on the card --
Name: " Joan Pelley "
Title : "Partner "
" Office: 202.555.0147 "
" Mobile: 202.555.0182 "

Backside of the card - solid medium color gray color w/ address and small message centered in the card - Trebuchet font
to read:

" 317 B North Linden Avenue, NE "
" Washington, DC 20099 "

Then below address to read:
" Fundraising | Event Planning | Political Consulting "

```html
<!DOCTYPE html>
<html lang="en">
<head>
<meta charset="utf-8">
<title>Silverfern Strategies – Business Card</title>
<link rel="stylesheet" href="https://fonts.googleapis.com/css2?family=Jura:wght@300;500;600&display=swap">
<style>
  :root {
    --backdrop: #e9e7e4;
    --card: #3c3c3e;
    --silver-light: #e6e6e8;
    --silver-mid: #b9babd;
    --silver-dark: #8e8f93;
    --band-shadow: #29292b;
    --ink-white: #f4f4f4;
    --ink-grey: #b4b4b6;
    --icon-glyph: #6b6c70;
  }
  * { box-sizing: border-box; margin: 0; padding: 0; }
  html, body { width: 1200px; height: 783px; overflow: hidden; background: var(--backdrop); }
  body { font-family: "Jura", "Trebuchet MS", sans-serif; position: relative; }

  .card {
    position: absolute;
    top: 86px;
    width: 350px;
    height: 612px;
    background: var(--card);
    border-radius: 6px;
    box-shadow: 0 14px 30px rgba(0,0,0,.22), 0 2px 4px rgba(0,0,0,.18);
    overflow: hidden;
  }
  .card--back { left: 190px; }
  .card--front { left: 660px; }

  /* Back side */
  .back-content {
    position: absolute; left: 0; right: 0; top: 200px;
    display: flex; flex-direction: column; align-items: center; text-align: center;
    padding: 0 16px;
  }
  .brand-dot { width: 46px; height: 46px; border-radius: 50%; background: var(--ink-white); flex: none; }
  .back-brand__name {
    color: var(--ink-white); font-weight: 300; font-size: 26px; letter-spacing: 4px; margin-top: 16px;
  }
  .back-address {
    font-style: normal; color: var(--ink-white); font-weight: 500;
    font-size: 13px; letter-spacing: 1px; line-height: 1.6; margin-top: 46px;
  }
  .back-services {
    color: var(--ink-grey); font-weight: 500; font-size: 10px; letter-spacing: .6px;
    margin-top: 18px; white-space: nowrap;
  }

  /* Front side */
  .silver-band {
    position: absolute; left: 26px; top: 0; bottom: 0; width: 52px;
    background: linear-gradient(90deg, var(--silver-dark), var(--silver-light) 45%, var(--silver-mid));
  }
  .silver-band::after {
    content: ""; position: absolute; top: 0; bottom: 0; right: -5px; width: 5px;
    background: var(--band-shadow);
  }
  .front-brand {
    position: absolute; left: 108px; top: 62px;
    display: flex; align-items: center; gap: 14px;
  }
  .front-brand .brand-dot { width: 34px; height: 34px; }
  .front-brand__text { color: var(--ink-grey); font-weight: 300; line-height: 1.15; }
  .front-brand__name { font-size: 24px; letter-spacing: 2px; }
  .front-brand__sub { font-size: 11px; letter-spacing: 3px; }

  .person { position: absolute; left: 108px; top: 196px; color: var(--ink-white); }
  .person__name { font-size: 27px; font-weight: 600; letter-spacing: 2px; }
  .person__title { font-size: 11px; font-weight: 500; letter-spacing: 1.5px; margin-top: 2px; }

  .contact-list { position: absolute; left: 0; top: 290px; width: 100%; list-style: none; }
  .contact-list li {
    position: relative; height: 50px; display: flex; align-items: center;
    padding-left: 108px; padding-right: 12px; color: var(--ink-white); font-weight: 500; letter-spacing: 1px;
    white-space: nowrap;
  }
  .contact-icon { position: absolute; left: 38px; top: 12px; width: 26px; height: 26px; }
  .contact--phone { font-size: 19px; letter-spacing: 2px; }
  .contact--mail, .contact--web { font-size: 14px; }
  .contact--address { font-size: 10.5px; }
</style>
</head>
<body>

  <section class="card card--back" aria-label="Card back">
    <div class="back-content">
      <span class="brand-dot"></span>
      <span class="back-brand__name">SILVERFERN</span>
      <address class="back-address">
        317 B North Linden Avenue, NE<br>
        Washington, DC 20099
      </address>
      <p class="back-services">Fundraising | Event Planning | Political Consulting</p>
    </div>
  </section>

  <section class="card card--front" aria-label="Card front">
    <div class="silver-band"></div>

    <div class="front-brand">
      <span class="brand-dot"></span>
      <div class="front-brand__text">
        <div class="front-brand__name">SILVERFERN</div>
        <div class="front-brand__sub">STRATEGIES</div>
      </div>
    </div>

    <div class="person">
      <div class="person__name">JOAN PELLEY</div>
      <div class="person__title">PARTNER</div>
    </div>

    <ul class="contact-list">
      <li class="contact--phone">
        <svg class="contact-icon" viewBox="0 0 26 26" aria-hidden="true">
          <circle cx="13" cy="13" r="13" fill="#f4f4f4"/>
          <path d="M9 7.5c.6-.5 1.4-.4 1.8.2l1 1.6c.3.5.2 1.1-.2 1.5l-.7.6c.6 1.4 1.6 2.5 3 3.1l.6-.7c.4-.4 1-.5 1.5-.2l1.6 1c.6.4.7 1.2.2 1.8l-.7.8c-.7.7-1.8.9-2.7.4-2.8-1.4-4.6-3.3-5.9-6-.4-.9-.2-2 .5-2.7z" fill="var(--icon-glyph)"/>
        </svg>
        202 555 0147
      </li>
      <li class="contact--phone">
        <svg class="contact-icon" viewBox="0 0 26 26" aria-hidden="true">
          <circle cx="13" cy="13" r="13" fill="#f4f4f4"/>
          <rect x="9.5" y="6.5" width="7" height="13" rx="1.4" fill="var(--icon-glyph)"/>
          <rect x="10.7" y="8" width="4.6" height="8.5" fill="#f4f4f4"/>
        </svg>
        202 555 0182
      </li>
      <li class="contact--mail">
        <svg class="contact-icon" viewBox="0 0 26 26" aria-hidden="true">
          <circle cx="13" cy="13" r="13" fill="#f4f4f4"/>
          <rect x="7" y="9" width="12" height="8.5" rx="1" fill="var(--icon-glyph)"/>
          <path d="M7.5 9.5l5.5 4.2 5.5-4.2" fill="none" stroke="#f4f4f4" stroke-width="1.2"/>
        </svg>
        joan@silverfernmail.com
      </li>
      <li class="contact--web">
        <svg class="contact-icon" viewBox="0 0 26 26" aria-hidden="true">
          <circle cx="13" cy="13" r="13" fill="#f4f4f4"/>
          <g fill="none" stroke="var(--icon-glyph)" stroke-width="1.3">
            <circle cx="13" cy="13" r="6"/>
            <ellipse cx="13" cy="13" rx="2.6" ry="6"/>
            <path d="M7 13h12"/>
          </g>
        </svg>
        www.silverfernstrategies.com
      </li>
      <li class="contact--address">
        <svg class="contact-icon" viewBox="0 0 26 26" aria-hidden="true">
          <circle cx="13" cy="13" r="13" fill="#f4f4f4"/>
          <path d="M13 6.5a4.5 4.5 0 0 1 4.5 4.5c0 3.3-4.5 8.5-4.5 8.5S8.5 14.3 8.5 11A4.5 4.5 0 0 1 13 6.5z" fill="var(--icon-glyph)"/>
          <circle cx="13" cy="11" r="1.7" fill="#f4f4f4"/>
        </svg>
        317 B North Linden Avenue, NE
      </li>
    </ul>
  </section>

</body>
</html>
```